Business card for a young aspring actress

My daughter is 18 and just starting out on her profession as an actress. She is a member of the Harbour Young Players and has already had some extras work and a featured role in an upcoming Feature film.

She wants/needs a card that she can have to hand to give to those she comes into contact with in the theatre, TV and film industries.

We are thinking that it may be double sided with an impact side including a picture of her and her name etc with the reverse holding contact and other details.

She wants to go by the name Maya Louise Brennick.

She has done a little modelling but sees herself as an actress.

She can be seen in this video
http://www.oakvalepark-academy.org/videos/be0881e4276ee2512c50a07f907c1d03?width=640&height=480

Target Market(s)

Anyone she comes into contact with in theatre TV and film industries.

Industry/Entity Type

Business

Requirements
Nice to have
• She has email and a website www.mayabrennick.com She is quite a connected girl

```html
<!DOCTYPE html>
<html lang="en">
<head>
<meta charset="utf-8">
<title>Maya Louise Brennick – actress</title>
<link rel="stylesheet" href="https://fonts.googleapis.com/css2?family=PT+Serif:wght@400&display=swap">
<style>
  :root {
    --card-black: #0b0b0b;
    --damask-tone: #1c1c1c;
    --cream: #ece8c8;
    --portrait-light: #f2f2f2;
    --portrait-mid: #b9b9b9;
    --portrait-dark: #6f6f6f;
  }
  * { margin: 0; padding: 0; box-sizing: border-box; }
  html, body {
    width: 1200px;
    height: 693px;
    overflow: hidden;
    background: var(--card-black);
  }
  .card {
    position: relative;
    width: 1200px;
    height: 693px;
    background: var(--card-black);
    overflow: hidden;
  }
  .damask-backdrop {
    position: absolute;
    inset: 0;
    background: radial-gradient(ellipse at 65% 45%, var(--damask-tone) 0%, var(--card-black) 75%);
  }
  .portrait {
    position: absolute;
    left: 0;
    top: 0;
    width: 500px;
    height: 693px;
  }
  .identity {
    position: absolute;
    left: 542px;
    width: 596px;
    top: 268px;
    text-align: center;
    font-family: "PT Serif", Georgia, serif;
    color: var(--cream);
  }
  .identity__name {
    font-weight: 400;
    font-size: 51px;
    line-height: 1;
    letter-spacing: 0.5px;
    white-space: nowrap;
  }
  .identity__rule {
    height: 3px;
    background: var(--cream);
    margin-top: 19px;
  }
  .identity__role {
    font-size: 37px;
    line-height: 1;
    margin-top: 27px;
    letter-spacing: 1px;
  }
</style>
</head>
<body>
  <main class="card">
    <div class="damask-backdrop" role="img" aria-label="Dark floral damask pattern background"></div>

    <svg class="portrait" viewBox="0 0 500 693" role="img" aria-label="Black and white portrait of the actress resting her face in her hands">
      <defs>
        <linearGradient id="portraitTone" x1="0" y1="0" x2="1" y2="0.3">
          <stop offset="0" stop-color="var(--portrait-mid)"/>
          <stop offset="0.45" stop-color="var(--portrait-light)"/>
          <stop offset="1" stop-color="var(--portrait-dark)"/>
        </linearGradient>
        <filter id="edgeShadow" x="-10%" y="-10%" width="130%" height="120%">
          <feDropShadow dx="4" dy="0" stdDeviation="6" flood-color="#000" flood-opacity="0.8"/>
        </filter>
      </defs>
      <polygon points="0,0 418,0 488,347 435,693 0,693" fill="url(#portraitTone)" filter="url(#edgeShadow)"/>
    </svg>

    <section class="identity">
      <h1 class="identity__name">Maya Louise Brennick</h1>
      <div class="identity__rule"></div>
      <p class="identity__role">- actress -</p>
    </section>
  </main>
</body>
</html>
```